Natural Skincare Company Needs Label Design

We need a label design for the first product of a new company called 'Vela'. We make skincare products made from natural ingredients.
Our initial product is a rose hip oil, and we need a label for the small 30mL bottle that it comes in, as well as for the box that the bottle will be sold in. The label will be printed directly onto the bottle, like the example in the attached photo. For reference, we like the look and feel of the labels on the bottle and box in the attached photos. It should convey a sense of natural.
The bottle will be dark green glass. For the name 'Vela' we like something close to orange so that it stands out. The rest of the text on the front of the bottle and box should read 'natural skincare' 'pure & organic' 'Rose hip oil' 'huile de cynorrhodon' 'pure et biologique'. '30mL' '1fl.oz'
We also like the silhouette of the main ingredient like in the attached photo. So a silhouette of a rose hip on the front of the bottle and box would be preferred.
On the right side of the bottle and box:
'Rose hip oil'
'Ingredients: 100% natural, cold pressed, Rosa canina (rose hip) seed oil'
'Benefits: Hydrates and refreshes skin, leaving a more even skin tone and a healthy glow'
'Application: Massage 3-4 drops into clean, damp skin twice daily or as required'
'Suitable for all skin types'
'Store below 30C'
On the left side of the bottle and box:
'Huile de Cynorrhodon'
'Ingredients/Constituants: huile de Rosa canina (cynorrhodon) 100% naturel, presse a froid'
'Bienfaits: rafraichit la peau, teint eblouissant'
'Mode d'emploi: Massez 3 a 4 gouttes sur une peau propre et humide deluxe fois par jour'
'Convient a tous les types de peau'
'Conserver a moins de 30C'

```html
<!DOCTYPE html>
<html lang="en">
<head>
<meta charset="utf-8">
<title>Vela Rose Hip Oil – Bottle and Box Labels</title>
<link rel="stylesheet" href="https://fonts.googleapis.com/css2?family=Cinzel:wght@400;600&display=swap">
<style>
  :root {
    --bg: #ffffff;
    --glass-green: #1f2a1f;
    --box-green: #2e3a2d;
    --box-green-side: #283327;
    --orange: #d98430;
    --grey-band: #c8c8c6;
    --band-text: #2a2a2a;
    --cream: #e9e4da;
  }
  * { box-sizing: border-box; margin: 0; padding: 0; }
  html, body { width: 1200px; height: 1005px; overflow: hidden; background: var(--bg); }
  body { position: relative; font-family: "Cinzel", "Times New Roman", serif; }

  .panel { position: absolute; display: flex; flex-direction: column; align-items: center; }

  .bottle-label { left: 215px; top: 460px; width: 250px; height: 400px; background: var(--glass-green); border-radius: 6px; padding-top: 30px; }
  .box-side { left: 560px; top: 60px; width: 215px; height: 900px; background: var(--box-green-side); padding-top: 40px; }
  .box-front { left: 775px; top: 40px; width: 270px; height: 920px; background: var(--box-green); padding-top: 50px; }

  .brand { color: var(--orange); font-weight: 600; letter-spacing: 0.04em; line-height: 1; display: flex; align-items: flex-start; gap: 5px; }
  .brand-dot { width: 8px; height: 8px; border-radius: 50%; background: var(--orange); margin-top: 4px; }

  .product { color: var(--orange); font-weight: 600; line-height: 1; margin-top: 22px; white-space: nowrap; }
  .product-fr { color: var(--orange); font-weight: 600; line-height: 1; margin-top: 4px; white-space: nowrap; }
  .product-fr small { font-size: 0.62em; }

  .band-grey { background: var(--grey-band); color: var(--band-text); text-align: center; margin-top: 14px; line-height: 1.35; white-space: nowrap; }
  .band-orange { background: var(--orange); color: var(--band-text); text-align: center; margin-top: 4px; padding: 4px 0 5px; line-height: 1.15; font-weight: 600; white-space: nowrap; }
  .band-orange small { font-size: 0.62em; }

  .volume { color: var(--cream); display: flex; gap: 30px; white-space: nowrap; }

  .sprig { background: linear-gradient(180deg, #c97a2c 0%, #b86c24 100%); opacity: 0.85; border-radius: 40% 40% 8px 8px; }

  /* bottle sizes */
  .bottle-label .brand { font-size: 40px; }
  .bottle-label .product { font-size: 19px; margin-top: 26px; }
  .bottle-label .product-fr { font-size: 14px; }
  .bottle-label .band-grey { width: 180px; font-size: 13px; margin-top: 20px; }
  .bottle-label .band-orange { width: 180px; font-size: 14px; }
  .bottle-label .volume { font-size: 15px; margin-top: 50px; }
  .bottle-label .sprig-left { position: absolute; left: 6px; top: 130px; width: 18px; height: 120px; }
  .bottle-label .sprig-right { position: absolute; right: 6px; top: 130px; width: 18px; height: 120px; }

  /* box side */
  .box-side .brand { font-size: 42px; }
  .box-side .product { font-size: 20px; margin-top: 28px; }
  .box-side .product-fr { font-size: 13px; }
  .box-side .band-grey { width: 150px; font-size: 12px; }
  .box-side .band-orange { width: 150px; font-size: 13px; }
  .box-side .sprig { width: 140px; height: 520px; margin-top: 40px; }

  /* box front */
  .box-front .brand { font-size: 64px; }
  .box-front .product { font-size: 28px; margin-top: 40px; }
  .box-front .product-fr { font-size: 19px; }
  .box-front .band-grey { width: 215px; font-size: 18px; margin-top: 20px; }
  .box-front .band-orange { width: 215px; font-size: 20px; }
  .box-front .sprig { width: 120px; height: 240px; margin-top: 40px; }
  .box-front .volume { font-size: 22px; margin-top: 40px; }
</style>
</head>
<body>
  <section class="panel bottle-label" aria-label="Bottle label">
    <div class="brand">Vela<span class="brand-dot"></span></div>
    <div class="product">ROSE HIP OIL</div>
    <div class="product-fr">HUILE <small>DE</small> CYNORRHODON</div>
    <div class="band-grey">NATURAL SKINCARE</div>
    <div class="band-orange">PURE <small>&amp;</small> ORGANIC<br>PURE <small>ET</small> BIOLOGIQUE</div>
    <div class="volume"><span>30ML</span><span>1FL.OZ</span></div>
    <div class="sprig sprig-left" role="img" aria-label="Rose hip branch silhouette in orange"></div>
    <div class="sprig sprig-right" role="img" aria-label="Rose hip branch silhouette in orange"></div>
  </section>

  <section class="panel box-side" aria-label="Box side panel">
    <div class="brand">Vela<span class="brand-dot"></span></div>
    <div class="product">ROSE HIP OIL</div>
    <div class="product-fr">HUILE <small>DE</small> CYNORRHODON</div>
    <div class="band-grey">NATURAL SKINCARE</div>
    <div class="band-orange">PURE <small>&amp;</small> ORGANIC<br>PURE <small>ET</small> BIOLOGIQUE</div>
    <div class="sprig" role="img" aria-label="Tall rose hip branch silhouette with leaves and hips in orange"></div>
  </section>

  <section class="panel box-front" aria-label="Box front panel">
    <div class="brand">Vela<span class="brand-dot"></span></div>
    <div class="product">ROSE HIP OIL</div>
    <div class="product-fr">HUILE <small>DE</small> CYNORRHODON</div>
    <div class="band-grey">NATURAL SKINCARE</div>
    <div class="band-orange">PURE <small>&amp;</small> ORGANIC<br>PURE <small>ET</small> BIOLOGIQUE</div>
    <div class="sprig" role="img" aria-label="Rose hip sprig silhouette with leaves and hips in orange"></div>
    <div class="volume"><span>30 ML</span><span>1FL.OZ</span></div>
  </section>
</body>
</html>
```